Have Logo - Need Business Card Design!!!

I am looking for a business card design for a real estate development business. The company name is Halvern Realty Partners. I already have a logo created by Sketch Harbor and would like this logo to be incorporated into the design. I have uploaded the files. The card needs to be professional, but visually interesting. Not necessary to be double-sided, but if you want to get creative and can think of something to put on the back then have at it.

Target Market(s)

The target audience for these business cards will be professionals in the real estate industry.

Industry/Entity Type

Real Estate

Requirements
Must have
• The business card must have all the necessary items for a business card, i.e. company name, our logo, name (however, not title necessary), office address, office phone number, cell number, fax number, website address, etc.

You can use the information below for the card:

Gregory L. Hanlon
782 Marlowe Avenue
San Francisco, California 94127

www.halvernrealty.example
ghanlon@mvrealtypartners.example
Office: 415-555-0142
Fax: 415-555-0143
Cell: 415-555-0186

```html
<!DOCTYPE html>
<html lang="en">
<head>
<meta charset="utf-8">
<title>Halvern Realty Partners – Business Card</title>
<link rel="stylesheet" href="https://fonts.googleapis.com/css2?family=Cinzel:wght@600&family=Arimo:wght@400&display=swap">
<style>
  :root {
    --backdrop: #2e2e2e;
    --card: #ffffff;
    --navy: #1f3f7a;
    --green: #1f8a3c;
    --ink: #1a1a1a;
  }
  html, body {
    margin: 0;
    width: 1200px;
    height: 456px;
    overflow: hidden;
    background: var(--backdrop);
  }
  .stage {
    position: relative;
    width: 1200px;
    height: 456px;
  }
  .card {
    position: absolute;
    left: 344px;
    top: 84px;
    width: 514px;
    height: 297px;
    background: var(--card);
    box-shadow: 0 2px 8px rgba(0,0,0,0.35);
  }
  .brand-name {
    position: absolute;
    left: 26px;
    top: 18px;
    margin: 0;
    font-family: "Cinzel", serif;
    font-weight: 600;
    font-size: 22px;
    line-height: 25px;
    color: var(--green);
    letter-spacing: 0.5px;
  }
  .address, .contact {
    position: absolute;
    left: 300px;
    font-family: "Arimo", Arial, sans-serif;
    font-size: 13.5px;
    line-height: 15.5px;
    color: var(--ink);
    font-style: normal;
  }
  .address { top: 55px; }
  .contact { top: 206px; }
  .contact .label { display: inline-block; width: 44px; }
  .person-name {
    position: absolute;
    left: 28px;
    top: 205px;
    margin: 0;
    font-family: "Cinzel", serif;
    font-weight: 600;
    font-size: 21px;
    line-height: 26px;
    color: var(--navy);
    letter-spacing: 0.3px;
  }
</style>
</head>
<body>
<main class="stage">
  <article class="card">
    <p class="brand-name">Halvern Realty<br>Partners</p>
    <address class="address">
      782 Marlowe Avenue<br>
      San Francisco, California 94127
    </address>
    <h1 class="person-name">Gregory L. Hanlon</h1>
    <div class="contact">
      <div>Office: 415-555-0142</div>
      <div><span class="label">Fax:</span>415-555-0143</div>
      <div><span class="label">Cell:</span>415-555-0186</div>
      <div>www.halvernrealty.example</div>
    </div>
  </article>
</main>
</body>
</html>
```